Business Card New Design for Corvella

We would like a new look on our business card, using the same style, the same colors blue, gray and white with similar font that is represented on the new Sell Sheet. We recently re-designed our Sell Sheets - I've attached a sell sheet file for your reference. I've also attached our current business card and our logo. Keep the same information listed on each side of the card.

Contact Information for Business Card

Use details given on example provided

Font styles to use
Other font styles liked:
• Myriad Regular and Bold

Colors

Designer to choose colors to be used in the design.

Requirements
Must have
• Current Information that was provided on the current business card. Colors Must use Blue, Gray and White, the same colors as the sell sheet example.

```html
<!DOCTYPE html>
<html lang="en">
<head>
<meta charset="utf-8">
<title>Corvella Technical Services – Business Card</title>
<link href="https://fonts.googleapis.com/css2?family=Source+Sans+3:wght@400;600;700&display=swap" rel="stylesheet">
<style>
  :root {
    --brand-blue: #3b55ad;
    --brand-blue-light: #4f6fc4;
    --ink-gray: #444548;
    --rule-gray: #55565a;
    --paper: #ffffff;
    --backdrop: #8f8e8f;
  }
  * { margin: 0; padding: 0; box-sizing: border-box; }
  html, body { width: 1200px; height: 900px; overflow: hidden; }
  body {
    background: var(--backdrop);
    font-family: "Source Sans 3", sans-serif;
    position: relative;
  }
  .card {
    position: absolute;
    left: 260px;
    width: 680px;
    height: 388px;
    border-radius: 26px;
    background: var(--paper);
    overflow: hidden;
    box-shadow: 0 6px 16px rgba(0,0,0,0.35);
  }
  .card--front { top: 40px; }
  .card--back { top: 472px; }

  /* Front */
  .front-identity {
    position: absolute;
    left: 60px; top: 0; width: 290px; height: 100%;
    display: flex; flex-direction: column; justify-content: center;
  }
  .brand-name {
    font-weight: 700;
    font-size: 48px;
    letter-spacing: 5px;
    color: var(--brand-blue);
    line-height: 1;
  }
  .company-name {
    margin-top: 18px;
    font-weight: 700;
    font-size: 30px;
    line-height: 1.1;
    color: var(--ink-gray);
  }
  .front-divider {
    position: absolute;
    left: 372px; top: 70px;
    width: 1.5px; height: 230px;
    background: var(--rule-gray);
  }
  .contact {
    position: absolute;
    left: 398px; top: 66px; width: 260px;
  }
  .contact-name {
    font-weight: 700; font-size: 27px; color: var(--brand-blue); line-height: 1.05;
  }
  .contact-title {
    font-weight: 400; font-size: 23px; color: var(--ink-gray); line-height: 1.1; margin-bottom: 8px;
  }
  .contact-address {
    font-weight: 700; font-size: 16px; color: var(--brand-blue);
    text-transform: uppercase; line-height: 1.3; margin-bottom: 6px;
  }
  .phone-list { list-style: none; }
  .phone-list li {
    display: flex; align-items: center; gap: 8px;
    font-weight: 600; font-size: 17px; color: var(--ink-gray); line-height: 1.45;
  }
  .phone-list svg { width: 20px; height: 20px; flex: none; }

  /* Back */
  .back-panel {
    position: absolute; right: 0; top: 0;
    width: 492px; height: 100%;
    background: radial-gradient(circle at 0% 0%, var(--brand-blue-light) 0%, var(--brand-blue) 55%);
  }
  .back-mark {
    position: absolute; left: 0; top: 0; width: 188px; height: 100%;
    display: flex; align-items: center; justify-content: center;
  }
  .back-mark span {
    transform: rotate(90deg);
    font-weight: 700; font-size: 44px; letter-spacing: 6px;
    color: var(--brand-blue); white-space: nowrap;
  }
  .service-list {
    list-style: none;
    position: absolute; left: 42px; top: 74px;
  }
  .service-list li {
    font-weight: 600; font-size: 19px; color: var(--paper);
    text-transform: uppercase; line-height: 1.5; letter-spacing: 0.3px;
  }
  .website {
    position: absolute; right: 34px; bottom: 30px;
    font-weight: 600; font-size: 16px; color: var(--paper); text-transform: uppercase;
  }
</style>
</head>
<body>

<section class="card card--front" aria-label="Business card front">
  <div class="front-identity">
    <div class="brand-name">CORVELLA</div>
    <div class="company-name">Corvella Technical<br>Services, inc.</div>
  </div>
  <div class="front-divider"></div>
  <div class="contact">
    <div class="contact-name">Marcus Hale</div>
    <div class="contact-title">CEO</div>
    <div class="contact-address">4180 Ridgeline Road<br>Oakmont IL 60599</div>
    <ul class="phone-list">
      <li>
        <svg viewBox="0 0 20 20" aria-hidden="true"><circle cx="10" cy="10" r="9" fill="none" stroke="var(--brand-blue)" stroke-width="1.6"/><path d="M6.5 5.5l2 0 1 2.5-1.3 1a6 6 0 0 0 2.8 2.8l1-1.3 2.5 1v2a1 1 0 0 1-1 1A8 8 0 0 1 5.5 6.5a1 1 0 0 1 1-1z" fill="var(--brand-blue)"/></svg>
        (800) 555-0142 X318
      </li>
      <li>
        <svg viewBox="0 0 20 20" aria-hidden="true"><circle cx="10" cy="10" r="9" fill="none" stroke="var(--brand-blue)" stroke-width="1.6"/><rect x="7" y="4.5" width="6" height="11" rx="1" fill="none" stroke="var(--brand-blue)" stroke-width="1.4"/><circle cx="10" cy="13.5" r="0.8" fill="var(--brand-blue)"/></svg>
        (630) 555-0142
      </li>
      <li>
        <svg viewBox="0 0 20 20" aria-hidden="true"><circle cx="10" cy="10" r="9" fill="none" stroke="var(--brand-blue)" stroke-width="1.6"/><rect x="5" y="9" width="10" height="6" rx="1" fill="var(--brand-blue)"/><rect x="7" y="5" width="6" height="4" fill="none" stroke="var(--brand-blue)" stroke-width="1.3"/></svg>
        (630) 555-0187
      </li>
      <li>
        <svg viewBox="0 0 20 20" aria-hidden="true"><circle cx="10" cy="10" r="9" fill="none" stroke="var(--brand-blue)" stroke-width="1.6"/><path d="M6.5 5.5l2 0 1 2.5-1.3 1a6 6 0 0 0 2.8 2.8l1-1.3 2.5 1v2a1 1 0 0 1-1 1A8 8 0 0 1 5.5 6.5a1 1 0 0 1 1-1z" fill="var(--brand-blue)"/></svg>
        (630) 555-0163
      </li>
    </ul>
  </div>
</section>

<section class="card card--back" aria-label="Business card back">
  <div class="back-mark"><span>CORVELLA</span></div>
  <div class="back-panel">
    <ul class="service-list">
      <li>Conveyors</li>
      <li>Target Sauce Appicators</li>
      <li>Target Topping Applicators</li>
      <li>Waterfall Topping Applicators</li>
      <li>Pepperoni/ Meat Slicer/ Applicators</li>
      <li>Portion Controlled Filler Pumps</li>
      <li>Check Weigh Conveyors</li>
      <li>Portion Compensators</li>
    </ul>
    <div class="website">www.c-t-s.com</div>
  </div>
</section>

</body>
</html>
```